Oven Cleaning Business owner needs business card design

Hi there,
Would like for a business card to be designed for myself, the owner of a professional oven cleaning business on the Sunshine Coast.
Would like it to look sleek, and modern-ish. Bit creative is encouraged too.
Include following:
Name/title: Corin ter Haghe, Owner
Phone number: 1300 482 916
Email: info@hearthshinecrew.com.au
Website: www.hearthshinecrew.com.au

```html
<!DOCTYPE html>
<html lang="en">
<head>
<meta charset="utf-8">
<title>Hearthshine Crew – Business Card</title>
<link href="https://fonts.googleapis.com/css2?family=Montserrat:wght@600;700&family=Questrial&display=swap" rel="stylesheet">
<style>
  :root {
    --backdrop: #d6d6d6;
    --paper: #ffffff;
    --ink: #0a0a0a;
    --aqua: #4fc3cc;
    --white: #ffffff;
  }
  * { margin: 0; padding: 0; box-sizing: border-box; }
  html, body { width: 1200px; height: 1200px; overflow: hidden; background: var(--backdrop); }
  .canvas { position: relative; width: 1200px; height: 1200px; }

  .card { position: absolute; overflow: hidden; }
  .card-front { left: 267px; top: 117px; width: 696px; height: 398px; background: var(--paper); }
  .card-back { left: 267px; top: 656px; width: 701px; height: 400px; background: var(--ink); }

  .brand { position: absolute; display: flex; align-items: center; gap: 16px; }
  .brand-dot { width: 64px; height: 64px; border-radius: 50%; background: var(--aqua); flex: none; }
  .brand-name {
    font-family: "Montserrat", sans-serif; font-weight: 700; font-size: 38px;
    line-height: 1.05; letter-spacing: 1px; text-transform: uppercase;
  }
  .card-front .brand { left: 145px; top: 42px; }
  .card-front .brand-name { color: var(--ink); }
  .card-back .brand { left: 145px; top: 75px; }
  .card-back .brand-dot { width: 80px; height: 80px; }
  .card-back .brand-name { color: var(--aqua); font-size: 44px; }

  .rule { position: absolute; left: 0; width: 100%; }
  .card-front .rule { top: 179px; height: 8px; background: var(--ink); }
  .card-back .rule { top: 253px; height: 6px; background: var(--aqua); }

  .person { position: absolute; right: 404px; top: 230px; text-align: right; }
  .person-name { font-family: "Montserrat", sans-serif; font-weight: 600; font-size: 26px; line-height: 36px; color: var(--ink); }
  .person-name .accent { color: var(--aqua); }
  .person-title { font-family: "Questrial", sans-serif; font-size: 21px; line-height: 26px; color: var(--aqua); }

  .divider { position: absolute; left: 307px; top: 238px; width: 2px; height: 81px; background: var(--ink); }

  .contacts { position: absolute; left: 326px; top: 242px; list-style: none; }
  .contacts li {
    display: flex; align-items: center; gap: 12px; height: 23.5px;
    font-family: "Questrial", sans-serif; font-size: 14px; color: var(--ink);
  }
  .contacts svg { width: 13px; height: 13px; flex: none; }

  .globe-badge {
    position: absolute; left: 334px; top: 240px; width: 32px; height: 32px;
    border-radius: 50%; background: var(--white); display: flex; align-items: center; justify-content: center;
  }
  .globe-badge svg { width: 22px; height: 22px; }
  .web-address {
    position: absolute; left: 0; width: 100%; top: 280px; text-align: center;
    font-family: "Questrial", sans-serif; font-size: 19px; color: var(--white); letter-spacing: 0.3px;
  }
</style>
</head>
<body>
<div class="canvas">

  <section class="card card-front">
    <div class="brand">
      <span class="brand-dot"></span>
      <span class="brand-name">Hearthshine<br>Crew</span>
    </div>
    <div class="rule"></div>

    <div class="person">
      <p class="person-name">Corin <span class="accent">ter</span><br>Haghe</p>
      <p class="person-title">Owner</p>
    </div>
    <div class="divider"></div>

    <ul class="contacts">
      <li>
        <svg viewBox="0 0 24 24"><path fill="var(--aqua)" d="M6.6 10.8a15 15 0 0 0 6.6 6.6l2.2-2.2c.3-.3.7-.4 1-.2 1.1.4 2.3.6 3.6.6.6 0 1 .4 1 1V20c0 .6-.4 1-1 1A17 17 0 0 1 3 4c0-.6.4-1 1-1h3.5c.6 0 1 .4 1 1 0 1.3.2 2.5.6 3.6.1.3 0 .7-.2 1z"/></svg>
        1300 482 916
      </li>
      <li>
        <svg viewBox="0 0 24 24"><rect x="2" y="5" width="20" height="14" rx="1.5" fill="var(--aqua)"/><path d="M3 6l9 7 9-7" fill="none" stroke="#fff" stroke-width="1.6"/></svg>
        info@hearthshinecrew.com.au
      </li>
      <li>
        <svg viewBox="0 0 24 24" fill="none" stroke="var(--aqua)" stroke-width="1.8"><circle cx="12" cy="12" r="9.5"/><ellipse cx="12" cy="12" rx="4.5" ry="9.5"/><path d="M2.5 12h19M4 7h16M4 17h16"/></svg>
        www.hearthshinecrew.com.au
      </li>
    </ul>
  </section>

  <section class="card card-back">
    <div class="brand">
      <span class="brand-dot"></span>
      <span class="brand-name">Hearthshine<br>Crew</span>
    </div>
    <div class="rule"></div>
    <div class="globe-badge">
      <svg viewBox="0 0 24 24" fill="none" stroke="var(--aqua)" stroke-width="1.6"><circle cx="12" cy="12" r="9.5"/><ellipse cx="12" cy="12" rx="4.5" ry="9.5"/><path d="M2.5 12h19M4 7h16M4 17h16"/></svg>
    </div>
    <p class="web-address">www.hearthshinecrew.com.au</p>
  </section>

</div>
</body>
</html>
```